Visitenkarten-Design für Ferienhausvermietung
Zielgruppe
Vermietung eines Ferienhauses
Aufgabenstellung
Die Visitenkarte sollte edel und hochwertig wirken...
Es wäre mir wichtig, dass die Visitenkarte im Querformat erstellt wird.
Die Farben vom Logo lauten:
green: C = 43 M = 0 Y = 100 N = 16
brown: C = 39 M = 57 J = 87 N = 53
sky blue: C = 14 M = 6 J = 6 N = 0
Aber bitte nicht so viel in den Visitenkarten verwenden. Die Visitenkarten sollen eher neutral gehalten werden.
Die Schriften
font
Lindeneck : Satisfaction
Ferienhaus : Corbert Regular
Flyer-Design für Ferienhausvermietung Flyer-Design für Ferienhausvermietung"
Es soll ein Flyer im Format DIN A4 erstellt werden. Der beidseitig bedruckt wird und dann 6seitig gefaltet wird. Ich benötige für den Flyer: Beschreibung/Ausstattung des Ferienhauses Beschreibung der Lage Beschreibung der Umgebung Anfahrt/Lage/Kontakt
Logo-Design für Ferienhaus ´Sa Morta´auf Mallorca mit eigenem Tennisplatz und Pool Logo-Design für Ferienhaus ´Sa Morta´auf Mallorca mit eigenem Tennisplatz und Pool"
Sie können sich meine Finca auf der Website: Casitorvent anschauen. Ort: Costitx Name des Hauses: Finca Reblat (heißt nur auf der Website so). Der Name am Tor Haus: Finca Sa Morta. Ich mag es gerne klassisch
Logo-Design für ein Feriendorf an der Ostsee Logo-Design für ein Feriendorf an der Ostsee"
* Nicht zu bunt, nicht zu verspielt, möglichst klar und aufgeräumt * In 2D, keine Schattierungen, keine Fotos im Hintergrund o. ä.. * Das Logo muss in allen Medien gut darstellbar sein! * Es sollte modern wirken, dennoch fröhlich, warm und einladend * Der Strand-/Wasserbezug muss deutlich we..
Flyer-Design für Ferienhaus Flyer-Design für Ferienhaus"
Flyerdesign für Ferienhaus: Din-Lang 2x gefalzt (übliche Format), 3 Seiten vorne und hinten.  Es sollte nach Möglichkeit an unsere Webseite (www.ferienhaus-kormoran-tidewik.de) angepasst werden, druckfertig sein und per PDF auf unserer Webseite zum Downloaden integriert werden können. Meh..
Logo-Design für Ferienhaus Logo-Design für Ferienhaus"
Wir suchen ein Moderenes Design gern berücksichtig in Kombination mit dem Naturpark Velmtaler Höhen. Da das Ferienhaus sich dort befindet.

```html
<!DOCTYPE html>
<html lang="de">
<head>
<meta charset="utf-8">
<title>Ferienhaus Lindeneck – Visitenkarte</title>
<link href="https://fonts.googleapis.com/css2?family=Allura&family=Open+Sans:wght@400&display=swap" rel="stylesheet">
<style>
  :root{
    --backdrop:#2b2e31;
    --sky:#dde6e5;
    --paper:#ffffff;
    --brown:#4a2f24;
    --green:#6d9b2c;
    --ink:#3e4650;
  }
  *{margin:0;padding:0;box-sizing:border-box}
  html,body{width:1200px;height:900px;overflow:hidden;background:var(--backdrop)}
  .canvas{position:relative;width:1200px;height:900px}
  .card{position:absolute;left:290px;width:620px;height:354px;background:var(--sky);overflow:hidden;
        box-shadow:0 6px 18px rgba(0,0,0,.35)}
  .card--front{top:76px}
  .card--back{top:470px}

  /* front: contact side */
  .front__band{position:absolute;left:0;right:0;bottom:0;height:120px;background:var(--paper)}
  .front__title{position:absolute;left:150px;top:112px;font-family:"Allura",cursive;font-size:62px;
        color:var(--brown);line-height:1;white-space:nowrap}
  .front__mark{position:absolute;left:440px;top:30px;width:76px;height:76px;border-radius:50%;
        border:2px solid var(--brown);background:var(--paper);display:flex;align-items:center;justify-content:center;
        font-family:"Open Sans",sans-serif;font-size:13px;color:var(--brown)}
  .front__address{position:absolute;left:170px;top:210px;background:var(--paper);padding:6px 16px;
        font-family:"Open Sans",sans-serif;font-size:15px;color:var(--ink)}
  .contact{position:absolute;display:flex;align-items:center;gap:7px;font-family:"Open Sans",sans-serif;
        font-size:15px;color:var(--ink)}
  .contact svg{width:13px;height:13px;flex:none}
  .contact--phone{left:220px;top:258px}
  .contact--mail{left:40px;top:305px}
  .contact--web{left:300px;top:305px}

  /* back: logo side */
  .back__band{position:absolute;left:0;right:0;top:100px;height:160px;background:var(--paper)}
  .back__mark{position:absolute;left:220px;top:67px;width:180px;height:180px;border-radius:50%;
        background:var(--paper);border:3px solid var(--brown);display:flex;align-items:center;justify-content:center;
        font-family:"Open Sans",sans-serif;font-size:28px;color:var(--brown)}
</style>
</head>
<body>
<main class="canvas">

  <section class="card card--front" aria-label="Visitenkarte Vorderseite">
    <div class="front__band"></div>
    <div class="front__mark">Lindeneck</div>
    <h1 class="front__title">Ferienhaus Lindeneck</h1>
    <p class="front__address">Erlenweg 12, 91234 Mittelbach</p>

    <p class="contact contact--phone">
      <svg viewBox="0 0 16 16" aria-hidden="true"><path fill="var(--green)" d="M3.5 1.5l2.5 0 1 3.5-1.8 1.2a8 8 0 0 0 4.6 4.6L11 9l3.5 1v2.5c0 1-1 2-2 2A11 11 0 0 1 1.5 3.5c0-1 1-2 2-2z"/></svg>
      09871/5520416
    </p>
    <p class="contact contact--mail">
      <svg viewBox="0 0 16 16" aria-hidden="true"><rect x="1" y="3" width="14" height="10" rx="1" fill="var(--green)"/><path d="M1.5 3.5L8 9l6.5-5.5" fill="none" stroke="#fff" stroke-width="1.3"/></svg>
      info@lindeneck-ferienhaus.de
    </p>
    <p class="contact contact--web">
      <svg viewBox="0 0 16 16" aria-hidden="true"><circle cx="8" cy="8" r="7" fill="var(--green)"/><path d="M1 8h14M8 1c-3 3-3 11 0 14M8 1c3 3 3 11 0 14" fill="none" stroke="#fff" stroke-width="1"/></svg>
      www.lindeneck-ferienhaus.de
    </p>
  </section>

  <section class="card card--back" aria-label="Visitenkarte Rückseite">
    <div class="back__band"></div>
    <div class="back__mark">Lindeneck</div>
  </section>

</main>
</body>
</html>
```